Removals & Storage a5 brochure required

We require a a4 1 fold into a5 brochure designed. we are an established removals and storage company based in southport, uk. we are looking for somthing we can take into more corporate offices ( estate agents etc) to show off what we do. our website has alot of information : www.haul-and-keep.co.uk which may be of use. we offer Domestic and Commercial removals & storage, packaging sales and services, 24/7 self storage options, mobile self storage. archive storage etc etc i have many files like logos etc where required. nice clean images / hgv with our image superimposed
Corporate, estate agents, domestic removals,
Designer to choose colors to be used in the design.

```html
<!DOCTYPE html>
<html lang="en">
<head>
<meta charset="utf-8">
<title>Seabrook Removals and Storage – A5 Brochure</title>
<link href="https://fonts.googleapis.com/css2?family=Montserrat:wght@500;600;700&family=Open+Sans:ital,wght@0,400;0,600;0,700;1,400&display=swap" rel="stylesheet">
<style>
  :root{
    --stage:#939393;
    --charcoal:#3d3d3d;
    --charcoal-deep:#353535;
    --yellow:#f7c51e;
    --white:#ffffff;
    --paper:#f1f1f1;
    --panel:#ececec;
    --ink:#2b2b2b;
    --muted:#cfcfcf;
  }
  *{box-sizing:border-box;margin:0;padding:0}
  html,body{width:1200px;height:1000px;overflow:hidden}
  body{background:var(--stage);font-family:"Open Sans",Arial,sans-serif;position:relative}
  .spread{position:absolute;left:296px;width:607px;display:flex;box-shadow:0 6px 18px rgba(0,0,0,.25)}
  .spread--outer{top:32px;height:463px}
  .spread--inner{top:517px;height:451px}
  .page{position:relative;width:303.5px;height:100%;overflow:hidden;background:var(--charcoal)}
  .page--front,.page--services{background:var(--charcoal-deep)}
  .web-bar{position:absolute;left:0;right:0;bottom:0;height:30px;background:var(--paper);display:flex;align-items:center;justify-content:center;font-family:"Montserrat",sans-serif;font-weight:600;font-size:8px;color:var(--ink)}
  .web-bar .hl{color:var(--yellow)}
  .web-bar--dark{background:var(--charcoal);color:var(--white);height:28px}
  .spread--inner .web-bar{height:28px}

  .brand{position:absolute;left:0;right:0;display:flex;align-items:center;justify-content:center;gap:6px}
  .brand__mark{width:14px;height:14px;background:var(--yellow)}
  .brand__name{font-family:"Montserrat",sans-serif;font-weight:700;color:var(--white);font-size:10px;line-height:1.1;text-transform:uppercase;letter-spacing:.3px}

  /* back cover */
  .page--back .brand{top:212px}
  .contact{position:absolute;top:286px;left:0;right:0;text-align:center;color:var(--white)}
  .contact__title{font-family:"Montserrat",sans-serif;font-weight:600;font-size:12px;color:var(--yellow);margin-bottom:14px}
  .contact__company{font-weight:700;font-size:6.5px;line-height:1.35}
  .contact__address{font-size:5.5px;line-height:1.4;color:var(--muted)}
  .contact__label{font-size:7px;margin-top:10px;color:var(--muted)}
  .contact__phone{font-family:"Montserrat",sans-serif;font-weight:700;font-size:11px;color:var(--yellow);margin-top:3px}
  .contact__email{font-size:6.5px;margin-top:2px}

  /* front cover */
  .page--front .brand{top:36px}
  .cover-photo{position:absolute;top:90px;left:0;right:0;height:250px;border-top:5px solid var(--yellow);border-bottom:5px solid var(--yellow);
    background:radial-gradient(circle at 50% 45%,#e6eef5 0,#9fb2c0 25%,#5b6b78 55%,#3b4651 100%)}
  .cover-title{position:absolute;top:362px;left:0;right:0;text-align:center;font-family:"Montserrat",sans-serif;font-weight:600;font-size:16.5px;line-height:1.35;color:var(--white)}

  /* inner left */
  .page--about{background:var(--panel)}
  .about-head{position:absolute;top:0;left:0;right:0;height:60px;background:var(--paper);display:flex;align-items:center;justify-content:space-between;padding:0 26px}
  .about-head__title{font-family:"Montserrat",sans-serif;font-weight:600;font-size:12.5px;line-height:1.3;color:var(--ink)}
  .about-head__tag{text-align:center;color:var(--ink)}
  .about-head__tag b{display:block;font-family:"Montserrat",sans-serif;font-weight:700;font-size:17px;letter-spacing:1px}
  .about-head__tag span{font-size:4.5px;font-weight:700;letter-spacing:.6px;text-transform:uppercase}
  .about-body{position:absolute;top:60px;left:0;right:0;height:148px;background:var(--charcoal);padding:14px 26px 0;color:var(--white)}
  .section-title{font-family:"Montserrat",sans-serif;font-weight:600;font-size:12.5px;color:var(--yellow);margin-bottom:8px}
  .about-body p{font-size:5.5px;line-height:1.45;margin-bottom:6px;color:#e2e2e2}
  .feature{position:absolute;left:166px;top:86px;width:118px}
  .feature__title{display:flex;align-items:center;gap:5px;font-weight:700;font-size:6.5px;margin-bottom:4px}
  .feature__text{font-size:5.3px;line-height:1.45;color:#e2e2e2;padding-left:15px}
  .photo{position:absolute;left:0;width:143px}
  .photo--mover{top:173px;height:110px;background:linear-gradient(135deg,#dfe5ea,#9aa7b2 55%,#c7a47a)}
  .photo--couple{top:291px;height:104px;background:linear-gradient(135deg,#d9d4cc,#8a8f98 55%,#c9a57a)}
  .services{position:absolute;left:165px;top:222px;width:125px}
  .services__title{font-family:"Montserrat",sans-serif;font-weight:600;font-size:12px;color:var(--ink);margin-bottom:10px}
  .services__list{list-style:none}
  .services__list li{position:relative;padding-left:9px;font-size:5.4px;line-height:1.35;color:var(--ink);margin-bottom:4.4px}
  .services__list li::before{content:"";position:absolute;left:0;top:2px;width:3px;height:3px;background:var(--yellow)}

  /* inner right */
  .service{position:absolute;left:32px;width:255px;display:flex;gap:18px}
  .service__icon{flex:0 0 36px;height:36px;border-radius:50%;background:var(--yellow);display:flex;align-items:center;justify-content:center}
  .service__title{font-family:"Montserrat",sans-serif;font-weight:600;font-size:11.5px;color:var(--yellow);margin-bottom:5px}
  .service__text{font-size:5.4px;line-height:1.45;color:#e2e2e2}
  .quote{position:absolute;left:32px;top:373px;width:240px;color:var(--white)}
  .quote__title{font-weight:700;font-size:7px;margin-bottom:4px}
  .quote__text{font-style:italic;font-size:5.4px;line-height:1.45}
</style>
</head>
<body>

<section class="spread spread--outer">
  <article class="page page--back">
    <div class="brand"><span class="brand__mark"></span><span class="brand__name">Seabrook<br>Removals &amp; Storage</span></div>
    <div class="contact">
      <h2 class="contact__title">Contact Us</h2>
      <p class="contact__company">Seabrook<br>Removals and Storage</p>
      <p class="contact__address">Unit 6, Kestrel Court,<br>Hartwell Industrial Estate L40 0ZZ</p>
      <p class="contact__label">Phone:</p>
      <p class="contact__phone">01632 960 104</p>
      <p class="contact__label">Email:</p>
      <p class="contact__email">info@haul-and-keep.co.uk</p>
    </div>
    <div class="web-bar">www.<span class="hl">haul-and-keep</span>.co.uk</div>
  </article>
  <article class="page page--front">
    <div class="brand"><span class="brand__mark"></span><span class="brand__name">Seabrook<br>Removals &amp; Storage</span></div>
    <div class="cover-photo" role="img" aria-label="Photo of a hand touching a tablet with glowing network points, warehouse blurred behind"></div>
    <h1 class="cover-title">Seabrook<br>Removals and Storage</h1>
    <div class="web-bar">www.<span class="hl">haul-and-keep</span>.co.uk</div>
  </article>
</section>

<section class="spread spread--inner">
  <article class="page page--about">
    <header class="about-head">
      <h2 class="about-head__title">Seabrook<br>Removals and Storage</h2>
      <div class="about-head__tag"><b>24/7</b><span>Self storage options</span></div>
    </header>
    <div class="about-body">
      <h3 class="section-title">About Us</h3>
      <p>Seabrook Removals and Storage provides seamless house removal and commercial business moves throughout the North west and nationwide.</p>
      <p>With more than two decades of experience within the moving and storage industry, Seabrook Removals and Storage provides a reliable, efficient service, ensuring our customers receive a quality service every time.</p>
      <div class="feature">
        <p class="feature__title">
          <svg width="10" height="10" viewBox="0 0 10 10"><circle cx="5" cy="5" r="4.3" fill="none" stroke="#f7c51e" stroke-width="1"/><path d="M2.8 5.1l1.5 1.5 3-3.2" fill="none" stroke="#f7c51e" stroke-width="1.2"/></svg>
          Professional Service
        </p>
        <p class="feature__text">Seabrook Removals and Storage are fully insured, holding a commercial insurance policy with leading insurance brokers.</p>
      </div>
    </div>
    <div class="photo photo--mover" role="img" aria-label="Photo of a removals worker carrying a cardboard box"></div>
    <div class="photo photo--couple" role="img" aria-label="Photo of a couple signing paperwork with a removals adviser"></div>
    <div class="services">
      <h3 class="services__title">Services</h3>
      <ul class="services__list">
        <li>Domestic removals</li>
        <li>Commercial relocations</li>
        <li>Worldwide shipping management</li>
        <li>Part loads nationwide</li>
        <li>Specialist antique, piano and heavy item transportation</li>
        <li>Domestic and commercial storage</li>
        <li>Dismantling and reassembling of furniture</li>
        <li>Full / Part packing / unpacking services</li>
        <li>Boxes and packaging materials</li>
        <li>Clearance, collection and disposal services</li>
        <li>Courier service</li>
      </ul>
    </div>
    <div class="web-bar web-bar--dark">www.<span class="hl">haul-and-keep</span>.co.uk</div>
  </article>

  <article class="page page--services">
    <div class="service" style="top:27px">
      <span class="service__icon"><svg width="18" height="18" viewBox="0 0 18 18" fill="none" stroke="#3d3d3d" stroke-width="1.4"><path d="M2 9l7-6 7 6"/><path d="M4 8v7h10V8"/><rect x="7.5" y="10.5" width="3" height="4.5"/></svg></span>
      <div><h3 class="service__title">House Removals</h3>
      <p class="service__text">We provide a full range of house removal services such as packing service, export wrapping of antique furniture, storage, specialist piano transportation, disposal of unwanted goods and many more services to complement your house move, we can tailor make your removal service to your individual requirements.</p></div>
    </div>
    <div class="service" style="top:100px">
      <span class="service__icon"><svg width="18" height="18" viewBox="0 0 18 18" fill="none" stroke="#3d3d3d" stroke-width="1.4"><rect x="3" y="3" width="8" height="12"/><rect x="11" y="7" width="4" height="8"/><path d="M5 6h4M5 9h4M5 12h4"/></svg></span>
      <div><h3 class="service__title">Commercial Removals</h3>
      <p class="service__text">We undertake specialist commercial office relocations for small and larger businesses. Seabrook Removals and Storage has experience in coordinating office/business relocations efficiently ensuring business continuity for your staff and organisation.</p></div>
    </div>
    <div class="service" style="top:167px">
      <span class="service__icon"><svg width="18" height="18" viewBox="0 0 18 18" fill="none" stroke="#3d3d3d" stroke-width="1.4"><rect x="3" y="2.5" width="12" height="13"/><path d="M3 9h12M9 2.5v13"/></svg></span>
      <div><h3 class="service__title">Storage solutions</h3>
      <p class="service__text">As the owner of Seabrook's largest storage facility we can easily arrange any storage requirements you may have be it short or long term storage of domestic or commercial goods.</p></div>
    </div>
    <div class="service" style="top:226px">
      <span class="service__icon"><svg width="20" height="18" viewBox="0 0 20 18" fill="none" stroke="#3d3d3d" stroke-width="1.4"><rect x="2" y="4" width="11" height="8"/><path d="M13 7h3l2 3v2h-5"/><circle cx="6" cy="13.5" r="1.6"/><circle cx="15" cy="13.5" r="1.6"/></svg></span>
      <div><h3 class="service__title">Mobile Self Storage</h3>
      <p class="service__text">Mobile Self Storage is a convenient, hassle free, simple way to store your goods. We deliver a mobile storage unit directly to your home or business, you load your goods into the storage unit then we take it away to our storage facility and store it. When you want your goods back just give us a call and we can arrange to deliver your unit back to you, SIMPLE!</p></div>
    </div>
    <div class="service" style="top:306px">
      <span class="service__icon"><svg width="18" height="18" viewBox="0 0 18 18" fill="none" stroke="#3d3d3d" stroke-width="1.4"><path d="M3 6l6-3 6 3v7l-6 3-6-3z"/><path d="M3 6l6 3 6-3M9 9v7"/></svg></span>
      <div><h3 class="service__title">Packing Service</h3>
      <p class="service__text">Here at Seabrook Removals and Storage, we can assist you by providing a flexible packing service to suit your needs and budget, our range of packing services ensure you get the help you require, at a cost you'll love</p></div>
    </div>
    <div class="quote">
      <p class="quote__title">FREE Quotations</p>
      <p class="quote__text">Whether you require storage, domestic / commercial removals or would like more details about our services. We can provide a FREE no obligation quotation.</p>
    </div>
    <div class="web-bar">www.<span class="hl">haul-and-keep</span>.co.uk</div>
  </article>
</section>

</body>
</html>
```